B2B telecom company need web design

We need a web design for our corporate web site. The company exists since almost 10 years.
This is a DESIGN contest, you're expected to provide design only, NOT the whole website. The winner will have to provide the HTML template (with Lorem Ipsum content) and the CSS files of his design.
Our initial product is SMS peering in P2P (you send a SMS to a friend in a foreign country, great chance that your operator route your SMS to us that we route to the recipient). We're launching a bulk SMS service (marketing and application to SMS).
Target is mostly corporate, usually big corporate (operators, contents providers...) where use of SMS is part of the main business.
The web site is composed of 1 landing page and 7 content pages (plan is given for your information, all content page are using the same template and the same design, you do NOT need to make one design per page) :
* About US
Company Profile
They trust us
The Volnor Team
Partners
Contact us
* Solution
P2P SMS
A2P SMS
You only need to submit the landing page and a template page for the content (with h1, h2, h3 and h4).
Design must be based on our new logo (see attached file).
Our current web site http://www.volnor-example.com
The winner of the contest will have to provide state of the art HTML template and CSS files of his design. Photo used shall be downloaded from Pixelbrook (provide the ID of the picture that we purchase file).
Target Market(s)
Telecom operator. SMS Peering hubs. Bulk SMS.
Industry/Entity Type
It Company
Number of Pages Required
2 page

```html
<!DOCTYPE html>
<html lang="en">
<head>
<meta charset="utf-8">
<title>Volnor — Africa &amp; Middle East Exchange</title>
<link rel="stylesheet" href="https://fonts.googleapis.com/css2?family=Montserrat:wght@400;600;700&family=PT+Sans:wght@400;700&family=Roboto:wght@400;500&display=swap">
<style>
:root{
  --green:#4a9e24;
  --green-dark:#3c8a1d;
  --lime:#8cc63e;
  --blue:#1a96cf;
  --blue-dark:#137fb3;
  --ink:#333336;
  --muted:#666;
  --light:#f6f3f3;
  --lavender:#eeeef5;
  --footer:#2b2b31;
  --footer-text:#9a9aa2;
  --red:#b33a1c;
  --orange:#e68a10;
}
*{box-sizing:border-box;margin:0;padding:0}
html,body{width:1200px;height:2528px;overflow:hidden}
body{position:relative;background:#fff;font-family:"PT Sans",Arial,sans-serif;color:var(--ink)}
.abs{position:absolute}
.photo{position:absolute}

/* header */
.site-header{position:absolute;left:0;top:0;width:1200px;height:74px;background:linear-gradient(#fff,#ececec)}
.brand{position:absolute;left:148px;top:20px;display:flex;align-items:center;gap:10px;font-family:"Montserrat",sans-serif;font-weight:600;font-size:26px;color:#55585c;letter-spacing:1px}
.brand-mark{width:14px;height:14px;background:var(--lime)}
.main-nav{position:absolute;left:0;top:30px;width:880px;height:16px;font-family:"Roboto",sans-serif;font-size:11px;color:#555}
.nav-link{position:absolute;top:0;white-space:nowrap}
.nav-link.current{color:var(--blue)}
.nav-sep{position:absolute;top:1px;width:1px;height:12px;background:#ddd}
.auth{position:absolute;top:23px;height:29px;color:#fff;font-family:"Roboto",sans-serif;font-size:12px;display:flex;align-items:center;gap:6px;padding-left:14px}
.auth.signup{left:888px;width:81px;background:var(--blue)}
.auth.login{left:969px;width:78px;background:var(--lime)}
.auth i{width:10px;height:10px;border:1.5px solid #fff;display:inline-block}

/* sub nav */
.sub-nav{position:absolute;left:0;top:74px;width:1200px;height:42px;background:linear-gradient(#27a6dc,#1387c0)}
.sub-item{position:absolute;top:0;height:42px;display:flex;align-items:center;gap:10px;color:#fff;font-family:"Roboto",sans-serif;font-size:10px;line-height:12px;border-left:1px solid rgba(255,255,255,.25);padding-left:26px}
.sub-item svg{flex:none}

/* hero */
.hero{position:absolute;left:0;top:116px;width:1200px;height:449px;background:radial-gradient(ellipse at 50% 40%,#55ad2b,var(--green) 60%,#3f9120)}
.hero-title{position:absolute;left:0;top:46px;width:1200px;text-align:center;font-family:"Montserrat",sans-serif;font-weight:700;font-size:30px;color:#fff;letter-spacing:.5px}
.hero-lead{position:absolute;left:280px;top:90px;width:640px;text-align:center;font-size:15px;line-height:19px;color:#fff}
.btn-light{position:absolute;left:541px;top:139px;width:118px;height:32px;background:#fff;color:#333;font-family:"Roboto",sans-serif;font-size:13px;display:flex;align-items:center;justify-content:center}
.hero-logo{position:absolute;left:430px;top:361px;width:269px;height:55px;background:#fff;border:3px solid var(--lime);display:flex;align-items:center;justify-content:center;gap:10px;font-family:"Montserrat",sans-serif;font-weight:600;font-size:24px;color:#55585c;letter-spacing:1px}

/* services */
.section-title{position:absolute;left:0;width:1200px;text-align:center;font-family:"Montserrat",sans-serif;font-weight:700;color:#3a3a3a}
.services-lead{position:absolute;left:360px;top:648px;width:480px;text-align:center;font-size:15px;line-height:18px;color:#555}
.service{position:absolute;top:720px;width:188px;height:188px;border-radius:50%;border:5px solid #e4e4e4;overflow:hidden}
.service.active{border-color:var(--lime)}
.service-num{position:absolute;width:40px;height:40px;border-radius:50%;background:#fff;border:3px solid #ccc;font-family:"Montserrat",sans-serif;font-weight:700;font-size:20px;color:#555;display:flex;align-items:center;justify-content:center}
.service-num.active{border-color:var(--lime)}
.service-label{position:absolute;top:934px;width:240px;text-align:center;font-family:"Montserrat",sans-serif;font-weight:600;font-size:16px;color:#3a3a3a}
.service-label.active{color:var(--lime)}

/* profile */
.profile{position:absolute;left:0;top:1011px;width:1200px;height:396px;background:var(--lavender);border-top:1px solid #e2e2e2}
.profile-kicker{position:absolute;left:689px;top:96px;font-family:"Montserrat",sans-serif;font-weight:700;font-size:20px;color:var(--green-dark)}
.profile-title{position:absolute;left:689px;top:127px;width:330px;font-family:"Montserrat",sans-serif;font-weight:600;font-size:19px;line-height:23px;color:#222}
.profile-text{position:absolute;left:689px;top:182px;width:370px;font-size:11.5px;line-height:17px;color:#333}
.play{position:absolute;left:689px;top:282px;display:flex;align-items:center;gap:10px;font-size:11px;font-style:italic;line-height:13px}
.play-box{width:38px;height:30px;border:2px solid #444;border-radius:3px;display:flex;align-items:center;justify-content:center;background:#fff}

/* team */
.team{position:absolute;left:0;top:1407px;width:1200px;height:480px;background:var(--light)}
.team-lead{position:absolute;left:0;top:92px;width:1200px;text-align:center;font-family:"Roboto",sans-serif;font-size:14px;color:#555}
.team-rule{position:absolute;left:148px;top:120px;width:910px;height:2px;background:linear-gradient(90deg,transparent,#d8d4d4 20%,#d8d4d4 80%,transparent)}
.team-head{position:absolute;left:148px;top:150px;width:282px;padding-bottom:10px;border-bottom:1px solid #ccc;font-family:"Montserrat",sans-serif;font-size:25px;font-weight:600;color:#333}
.team-head small{font-size:14px;font-weight:400}
.team-text{position:absolute;left:148px;top:202px;width:285px;font-size:11.5px;line-height:16.6px;color:#444}
.btn-red{position:absolute;left:148px;top:381px;width:111px;height:29px;background:var(--red);color:#fff;font-size:14px;display:flex;align-items:center;justify-content:center}
.member{position:absolute;top:155px;width:165px;height:253px}
.member-overlay{position:absolute;left:0;bottom:0;width:165px;height:96px;background:rgba(0,0,0,.55);color:#fff;text-align:center;font-size:10.5px;line-height:13px;padding-top:12px}
.member-overlay .icons{display:flex;justify-content:center;gap:6px;margin-bottom:10px}
.member-overlay .icons i{width:20px;height:20px;border-radius:50%;border:1.5px solid #fff;display:block}

/* partners */
.partners{position:absolute;left:0;top:1887px;width:1200px;height:384px;background:#fff;border:1px solid #ddd}
.partners-title{position:absolute;left:0;top:34px;width:1200px;text-align:center;font-family:"Montserrat",sans-serif;font-weight:600;font-size:28px;color:var(--blue-dark)}
.partner{position:absolute;top:100px;width:148px;height:148px;border-radius:50%;background:radial-gradient(circle at 50% 40%,#fff 60%,#f0f0f0);box-shadow:0 3px 10px rgba(0,0,0,.1);display:flex;align-items:center;justify-content:center;font-family:"PT Sans",sans-serif;font-weight:700;font-size:20px;color:#333}
.partner-name{position:absolute;top:270px;width:200px;text-align:center;font-family:"Roboto",sans-serif;font-size:19px;color:#555}
.partner-name.active{color:var(--blue)}
.partner-note{position:absolute;top:297px;width:200px;text-align:center;font-size:10.5px;line-height:14px;color:#555}
.arrow{position:absolute;top:172px}

/* footer */
.site-footer{position:absolute;left:0;top:2271px;width:1200px;height:257px;background:var(--footer);color:var(--footer-text);font-family:"Roboto",sans-serif}
.foot-head{position:absolute;top:44px;font-size:12.5px;font-weight:500;color:#fff}
.foot-list{position:absolute;top:80px;font-size:9.5px;line-height:20px;list-style:none}
.foot-text{position:absolute;left:327px;top:80px;width:270px;font-size:9.5px;line-height:13px}
.btn-orange{position:absolute;left:327px;top:157px;width:67px;height:17px;background:var(--orange);color:#fff;font-size:8px;display:flex;align-items:center;justify-content:center}
.contact-row{position:absolute;left:689px;display:flex;gap:10px;font-size:9.5px;line-height:12px}
.phone{position:absolute;left:707px;top:152px;font-size:15px;font-weight:500;color:#fff}
.social{position:absolute;left:928px;display:flex;align-items:center;gap:12px;font-size:9.5px}
.social i{width:10px;height:10px;background:var(--footer-text);display:block}
.foot-rule{position:absolute;left:148px;top:206px;width:900px;height:1px;background:#3d3d44}
.copyright{position:absolute;left:148px;top:226px;font-size:9.5px}
.legal{position:absolute;left:912px;top:226px;font-size:9.5px}
</style>
</head>
<body>

<header class="site-header">
  <div class="brand"><span>VOLNOR</span><span class="brand-mark"></span></div>
  <nav class="main-nav">
    <span class="nav-link current" style="left:542px">HOME</span>
    <span class="nav-sep" style="left:588px"></span>
    <span class="nav-link" style="left:603px">ABOUT</span>
    <span class="nav-sep" style="left:653px"></span>
    <span class="nav-link" style="left:669px">NEWS</span>
    <span class="nav-sep" style="left:714px"></span>
    <span class="nav-link" style="left:729px">LOCATIONS</span>
    <span class="nav-sep" style="left:806px"></span>
    <span class="nav-link" style="left:820px">CONTACT</span>
  </nav>
  <div class="auth signup"><i></i>Sign up</div>
  <div class="auth login"><i></i>Log in</div>
</header>

<nav class="sub-nav">
  <div class="sub-item" style="left:150px;width:188px"><svg width="14" height="22" viewBox="0 0 14 22"><rect x="1" y="1" width="12" height="20" rx="2" fill="none" stroke="#fff" stroke-width="2"/><rect x="3" y="4" width="8" height="11" fill="#fff"/></svg><span>Mobile<br>EXCHANGE</span></div>
  <div class="sub-item" style="left:338px;width:180px"><svg width="14" height="22" viewBox="0 0 14 22"><rect x="1" y="1" width="12" height="20" rx="2" fill="none" stroke="#fff" stroke-width="2"/><rect x="3" y="4" width="8" height="11" fill="#fff"/></svg><span>Mobile<br>ADVANTAGE</span></div>
  <div class="sub-item" style="left:518px;width:190px"><svg width="14" height="22" viewBox="0 0 14 22"><rect x="1" y="1" width="12" height="20" rx="2" fill="none" stroke="#fff" stroke-width="2"/><rect x="3" y="4" width="8" height="11" fill="#fff"/></svg><span>Mobile<br>INTEROPERABILITY</span></div>
  <div class="sub-item" style="left:708px;width:190px"><svg width="14" height="22" viewBox="0 0 14 22"><rect x="1" y="1" width="12" height="20" rx="2" fill="none" stroke="#fff" stroke-width="2"/><rect x="3" y="4" width="8" height="11" fill="#fff"/></svg><span>Mobile<br>SOLUTIONS</span></div>
  <div class="sub-item" style="left:898px;width:152px;border-right:1px solid rgba(255,255,255,.25)"><svg width="24" height="20" viewBox="0 0 24 20"><rect x="1" y="4" width="8" height="15" rx="1" fill="#fff"/><rect x="12" y="1" width="10" height="18" rx="1" fill="none" stroke="#fff" stroke-width="2"/></svg><span>TECHNOLOGY</span></div>
</nav>

<section class="hero">
  <h1 class="hero-title">AFRICA &amp; MIDDLE EAST EXCHANGE</h1>
  <p class="hero-lead">Volnor Mobile Exchange is the combination of world-class enterprise solutions and an unrivaled global data network, creating one of the global leader in mobile.</p>
  <div class="btn-light">Read More</div>
  <div class="photo" role="img" aria-label="Businesswoman reading a text message on her phone" style="left:150px;top:300px;width:241px;height:149px;background:linear-gradient(135deg,#8a8276,#d9cfc2 45%,#2a2a2a)"></div>
  <div class="photo" role="img" aria-label="Woman using a phone in the back seat of a car" style="left:393px;top:187px;width:188px;height:172px;background:linear-gradient(160deg,#1e1e22,#c8a38c 50%,#d04a74)"></div>
  <div class="photo" role="img" aria-label="Car interior detail" style="left:393px;top:359px;width:37px;height:90px;background:linear-gradient(#444,#1a1a1a)"></div>
  <div class="photo" role="img" aria-label="Map graphic with message exchange arrows" style="left:585px;top:263px;width:106px;height:93px;background:linear-gradient(135deg,#7bbf4a,#3a7d1f);border:1px solid #fff"></div>
  <div class="photo" role="img" aria-label="Smiling senior couple holding mobile phones" style="left:696px;top:229px;width:182px;height:220px;background:linear-gradient(160deg,#111,#3a3330 40%,#c9b7a8 60%,#111)"></div>
  <div class="photo" role="img" aria-label="Man talking on a mobile phone" style="left:881px;top:300px;width:167px;height:149px;background:linear-gradient(135deg,#b8b0a4,#3b2c22 50%,#6a7f3a)"></div>
  <div class="hero-logo"><span>VOLNOR</span><span class="brand-mark"></span></div>
</section>

<section>
  <h2 class="section-title" style="top:608px;font-size:30px">OUR SERVICES</h2>
  <p class="services-lead">Every day, the mobile landscape evolves. Today's subscribers use mobile handsets for a wide variety of communications.</p>
  <svg class="abs" style="left:430px;top:810px" width="80" height="8"><line x1="0" y1="4" x2="80" y2="4" stroke="#999" stroke-width="5" stroke-dasharray="4 2"/></svg>
  <svg class="abs" style="left:700px;top:810px" width="80" height="8"><line x1="0" y1="4" x2="80" y2="4" stroke="#999" stroke-width="5" stroke-dasharray="4 2"/></svg>
  <div class="service" style="left:240px" role="img" aria-label="Businesswoman using a phone"><div style="width:100%;height:100%;background:linear-gradient(135deg,#bdb6ac,#e6d9c6 45%,#1e1e1e)"></div></div>
  <div class="service active" style="left:508px" role="img" aria-label="Senior couple holding phones"><div style="width:100%;height:100%;background:linear-gradient(160deg,#111,#4a3e38 45%,#cbb9aa 60%,#111)"></div></div>
  <div class="service" style="left:781px" role="img" aria-label="Man making a phone call"><div style="width:100%;height:100%;background:linear-gradient(135deg,#9c9890,#3a2b22 50%,#d8d4cc)"></div></div>
  <div class="service-num" style="left:379px;top:722px">1</div>
  <div class="service-num active" style="left:648px;top:722px">2</div>
  <div class="service-num" style="left:920px;top:722px">3</div>
  <div class="service-label" style="left:214px">OPERATOR</div>
  <div class="service-label active" style="left:482px">BRAND &amp; CONTENT</div>
  <div class="service-label" style="left:755px">ENTERPRISE</div>
</section>

<section class="profile">
  <div class="photo" role="img" aria-label="Young professional with laptop in a glass office" style="left:0;top:0;width:700px;height:395px;background:linear-gradient(90deg,#8a8a86 0%,#cfd6dc 30%,#9aa7ae 55%,#d8e0e6 80%,var(--lavender) 100%)"></div>
  <h3 class="profile-kicker">COMPANY PROFILE</h3>
  <h2 class="profile-title">Lorem Ipsum is that it has a but normal distribution.</h2>
  <p class="profile-text">There are many variations of passages of Lorem Ipsum available, but the majority have suffered alteration in some form, by injected humour, or randomised words which don't look even slightly believable. If you are going to use a passage of Lorem Ipsum, you need to be sure there isn't anything embarrassing hidden in the middle of text.</p>
  <div class="play"><div class="play-box"><svg width="14" height="14" viewBox="0 0 14 14"><path d="M2 1 L13 7 L2 13Z" fill="#d22"/></svg></div><span>Play Our<br>Testing Video</span></div>
</section>

<section class="team">
  <h2 class="section-title" style="top:50px;font-size:24px;font-weight:600">The Volnor Team</h2>
  <p class="team-lead">It is a long established fact that a reader will be distracted by the readable content</p>
  <div class="team-rule"></div>
  <h3 class="team-head">LOREM IP.<small>(There are many)</small></h3>
  <p class="team-text">There are many variations of passages of Lorem Ipsum available, but the majority have suffered alteration in some form, by injected humour,or randomised words which don't look even slightly believable. If you are going to use a passage of Lorem Ipsum, you need to be sure there isn't anything embarrassing hidden in the middle of text.All the Lorem Ipsum generators on the Internet tend to repeat predefined chunks as necessary, making this the first true generator on the Internet. It uses a dictionary of over 200 Latin words,</p>
  <div class="btn-red">Learn More</div>
  <div class="member" style="left:507px" role="img" aria-label="Portrait of a team member in a dark suit"><div style="width:100%;height:100%;background:linear-gradient(#bdbdbd,#2a2a2a 60%,#111)"></div>
    <div class="member-overlay"><div class="icons"><i></i><i></i><i></i><i></i></div>Lorem Ipsum is simply dummy<br>text typesetting industry.</div></div>
  <div class="member" style="left:698px" role="img" aria-label="Portrait of a team member in a white blazer"><div style="width:100%;height:100%;background:linear-gradient(135deg,#3a2a24,#d9c3a6 45%,#efefef)"></div></div>
  <div class="member" style="left:883px" role="img" aria-label="Portrait of a team member in a dark jacket"><div style="width:100%;height:100%;background:linear-gradient(135deg,#6a4a3a,#c89a7c 45%,#222)"></div></div>
</section>

<section class="partners">
  <h2 class="partners-title">Partners</h2>
  <svg class="arrow" style="left:108px" width="12" height="20"><path d="M10 2 L2 10 L10 18" fill="none" stroke="#bbb" stroke-width="2"/></svg>
  <svg class="arrow" style="left:1078px" width="12" height="20"><path d="M2 2 L10 10 L2 18" fill="none" stroke="var(--blue)" stroke-width="2"/></svg>
  <div class="partner" style="left:145px">Verdane</div>
  <div class="partner" style="left:335px">Lumora</div>
  <div class="partner" style="left:528px">Brightel</div>
  <div class="partner" style="left:721px">Northis</div>
  <div class="partner" style="left:912px">Northis</div>
  <div class="partner-name" style="left:119px">Verdane</div>
  <div class="partner-name" style="left:309px">Lumora</div>
  <div class="partner-name active" style="left:502px">Brightel</div>
  <div class="partner-name" style="left:695px">Northis</div>
  <div class="partner-name" style="left:886px">Northis</div>
  <p class="partner-note" style="left:119px">Lorem Ipsum is simply dummy<br>text of the printing</p>
  <p class="partner-note" style="left:309px">Lorem Ipsum is simply dummy<br>text of the printing</p>
  <p class="partner-note" style="left:502px">Lorem Ipsum is simply dummy<br>text of the printing</p>
  <p class="partner-note" style="left:695px">Lorem Ipsum is simply dummy<br>text of the printing</p>
  <p class="partner-note" style="left:886px">Lorem Ipsum is simply dummy<br>text of the printing</p>
</section>

<footer class="site-footer">
  <h4 class="foot-head" style="left:148px">Site Map</h4>
  <ul class="foot-list" style="left:148px"><li>› Home</li><li>› About Us</li><li>› News</li><li>› Locations</li><li>› Contact Us</li></ul>
  <h4 class="foot-head" style="left:327px">Lorem Ipsum available.</h4>
  <p class="foot-text">There are many variations of passages of Lorem Ipsum available, but the majority have suffered alteration in some form, by injected humour, or randomised words which don't look even slightly believable. If you are going to use a passage of Lorem Ipsum, you need to be sure there isn't anything</p>
  <div class="btn-orange">LEARN MORE</div>
  <h4 class="foot-head" style="left:689px">Contact Us</h4>
  <div class="contact-row" style="top:84px"><svg width="8" height="12" viewBox="0 0 8 12"><path d="M4 0a4 4 0 0 1 4 4c0 3-4 8-4 8S0 7 0 4a4 4 0 0 1 4-4z" fill="#9a9aa2"/></svg><span><b style="color:#ccc;font-weight:500">KESTREL HOUSE</b><br>12 Harbour Lane<br>Suite 400 Westport</span></div>
  <div class="contact-row" style="top:135px"><svg width="11" height="8"><rect x=".5" y=".5" width="10" height="7" fill="none" stroke="#9a9aa2"/><path d="M.5 .5 5.5 4.5 10.5 .5" fill="none" stroke="#9a9aa2"/></svg><span>info@volnor-example.com</span></div>
  <svg class="abs" style="left:689px;top:154px" width="11" height="12" viewBox="0 0 11 12"><path d="M2 0h2l1 3-1.5 1a7 7 0 0 0 3.5 3.5L8 6l3 1v2c0 1-1 2-2 2A9 9 0 0 1 0 2c0-1 1-2 2-2z" fill="#9a9aa2"/></svg>
  <div class="phone">555-010-4477</div>
  <h4 class="foot-head" style="left:918px">We are Social</h4>
  <div class="social" style="top:84px"><i></i>Fan us on Friendspace</div>
  <div class="social" style="top:106px"><i></i>Follow us on Chirper</div>
  <div class="social" style="top:128px"><i></i>Fan us on Worklink</div>
  <div class="social" style="top:150px"><i></i>Join in to Viewtube</div>
  <div class="foot-rule"></div>
  <p class="copyright">© Copyrights volnor-example.com 2015. All rights reserved.</p>
  <p class="legal">Terms and Conditions &nbsp;|&nbsp; Privacy</p>
</footer>

</body>
</html>
```